Website Re-Design

We would like to explore the possibility of a re-design of our website. We want all the content that it currently has to remain on the pages, and we don't want our logo/corporate identity or colours changed, so it is literally just a website re-design.

Our website is www.drelvix.co.uk

Websites that we like are

http://www.tarnwillow.co.uk/
http://quomplet.com/

```html
<!DOCTYPE html>
<html lang="en">
<head>
<meta charset="utf-8">
<title>Drelvix – Inbound Marketing &amp; SEO Performance Agency</title>
<link href="https://fonts.googleapis.com/css2?family=Arimo:wght@400;700&family=Oswald:wght@400;500&display=swap" rel="stylesheet">
<style>
:root{
  --magenta:#c8157a;
  --green:#8bc249;
  --green-dark:#6da52f;
  --teal:#1cb3a6;
  --ink:#222;
  --text:#444;
  --grey-band:#e9e9e9;
  --navy:#2b3142;
  --footer:#111;
  --footer-line:#2a2a2a;
  --footer-text:#9a9a9a;
  --white:#fff;
}
*{box-sizing:border-box;margin:0;padding:0}
html,body{width:1200px;height:2652px;overflow:hidden}
body{position:relative;background:var(--white);font-family:"Arimo",Arial,sans-serif;color:var(--text)}
.abs{position:absolute}
a{color:inherit;text-decoration:none}

/* header + hero */
.hero{left:0;top:0;width:1200px;height:542px;background:radial-gradient(ellipse at 55% 55%,#6d6d6d 0%,#3a3a3a 40%,#111 80%)}
.topbar{left:0;top:0;width:1200px;height:82px;background:rgba(0,0,0,.78)}
.brand{font-family:"Arimo",Arial,sans-serif;font-weight:700;color:var(--magenta);letter-spacing:1px}
.topbar .brand{left:146px;top:18px;font-size:34px}
.top-contact{top:8px;font-size:14px;color:var(--green);display:flex;align-items:center;gap:8px}
.nav{top:49px;left:537px;display:flex;gap:0;font-size:14px;color:var(--white)}
.nav a{position:absolute;white-space:nowrap}
.nav a.active::after{content:"";position:absolute;left:-4px;right:-4px;top:28px;height:3px;background:var(--green)}

/* intro */
.intro-logo{left:0;width:1200px;top:580px;text-align:center;font-size:44px}
.tagline{left:0;width:1200px;top:634px;text-align:center;font-size:23px;color:var(--ink)}
.intro-copy{left:320px;width:560px;top:680px;text-align:center;font-size:13px;line-height:21px;color:var(--text)}
.intro-shadow{left:250px;width:700px;top:770px;height:30px;background:radial-gradient(ellipse at 50% 0,rgba(0,0,0,.18),rgba(0,0,0,0) 70%)}

/* feature tiles */
.tile{top:869px;width:303px;height:163px;color:var(--white)}
.tile--services{left:141px;background:var(--magenta)}
.tile--portfolio{left:449px;background:var(--green)}
.tile--talk{left:756px;background:var(--teal)}
.tile svg{position:absolute;left:14px;top:20px}
.tile-copy{position:absolute;left:118px;top:18px;width:170px;font-size:12.5px;line-height:17px}
.tile-title{position:absolute;left:14px;bottom:10px;font-family:"Oswald",Arial,sans-serif;font-weight:500;font-size:19px;text-transform:uppercase}

/* recent work */
.work{left:0;top:1090px;width:1200px;height:435px;background:var(--grey-band)}
.section-title{font-size:27px;font-weight:700}
.work .section-title{left:141px;top:48px;color:var(--green)}
.work-copy{left:141px;top:103px;width:300px;font-size:13.5px;line-height:22px;color:var(--text)}
.monitor{left:515px;top:48px;width:491px;height:297px;background:#161616;border-radius:10px}
.monitor-screen{left:530px;top:64px;width:461px;height:262px;background:linear-gradient(180deg,#2c3b52 0%,#e2b23a 55%,#c98a1f 100%)}
.monitor-stand{left:700px;top:345px;width:120px;height:46px;background:linear-gradient(#ddd,#b9b9b9);clip-path:polygon(18% 0,82% 0,100% 100%,0 100%)}
.chevron{top:170px}

/* clients */
.clients{left:0;top:1525px;width:1200px;height:287px;background:var(--navy)}
.clients .section-title{left:141px;top:44px;color:var(--white)}
.clients-copy{left:141px;top:95px;width:300px;font-size:13.5px;line-height:21px;color:#d6d9e0}
.slider-btn{top:214px;width:34px;height:36px;background:#6a7182}
.client{top:91px;width:188px;height:128px;background:var(--white);display:flex;align-items:center;justify-content:center;gap:10px;font-size:22px;font-weight:700;color:#3b3f4a}
.client i{display:block;width:14px;height:14px;border-radius:50%;background:#3b3f4a}

/* call to action */
.cta .section-title{left:141px;top:1848px;color:var(--green)}
.cta-sub{left:141px;top:1890px;font-size:21px;color:var(--ink)}
.cta-copy{left:141px;top:1924px;width:620px;font-size:13.5px;line-height:19px;color:var(--text)}
.cta-btn{left:805px;top:1898px;width:225px;height:60px;background:linear-gradient(#8fd04a,#4f9a1e);border:2px solid #3f7f15;border-radius:4px;color:var(--white);font-size:26px;font-weight:700;display:flex;align-items:center;justify-content:center}

/* footer */
.footer{left:0;top:2051px;width:1200px;height:601px;background:var(--footer);color:var(--footer-text)}
.to-top{left:578px;top:2030px;width:42px;height:42px;border-radius:50%;background:var(--white);border:3px solid var(--footer)}
.footer-title{left:0;width:1200px;text-align:center;color:var(--white);font-size:29px;font-weight:700;top:2084px}
.footer-sub{left:0;width:1200px;text-align:center;color:var(--magenta);font-size:21px;font-weight:700;top:2136px}
.footer-intro{left:200px;width:800px;text-align:center;top:2180px;font-size:13px;line-height:20px}
.rule{height:1px;background:var(--footer-line)}
.vrule{width:1px;background:var(--footer-line)}
.f-head{font-size:13.5px;font-weight:700;color:var(--green);text-transform:uppercase}
.f-body{font-size:13px;line-height:20px}
.f-big{font-size:17px;color:#d8d8d8}
.social{display:flex;gap:12px;top:2292px;left:857px}
.social i{display:block;width:18px;height:18px;border-radius:50%;background:#777}
.links{list-style:none;font-size:13px;line-height:21px;color:#d0d0d0;text-transform:uppercase}
.search-input{left:857px;top:2424px;width:202px;height:34px;background:#9a9a9a;border-radius:3px;color:#222;font-size:12px;padding:10px 8px}
.search-btn{left:857px;top:2469px;width:89px;height:33px;background:#d2d2d2;border-radius:3px;color:#222;font-size:12px;font-weight:700;display:flex;align-items:center;justify-content:center}
.footer-brand{left:141px;top:2590px;font-size:36px}
.legal{left:302px;top:2584px;width:760px;font-size:12.5px;line-height:19px}
</style>
</head>
<body>

<div class="abs hero" role="img" aria-label="Black and white photo of a hand touching a glowing network of social media icons around a central brand circle"></div>
<header class="abs topbar">
  <div class="abs brand">DRELVIX</div>
  <div class="abs top-contact" style="left:696px">
    <svg width="14" height="14" viewBox="0 0 24 24"><path fill="var(--green)" d="M6.6 10.8a15 15 0 0 0 6.6 6.6l2.2-2.2c.3-.3.7-.4 1-.2 1.1.4 2.3.6 3.6.6.6 0 1 .4 1 1V20c0 .6-.4 1-1 1A17 17 0 0 1 3 4c0-.6.4-1 1-1h3.5c.6 0 1 .4 1 1 0 1.3.2 2.5.6 3.6.1.3 0 .7-.2 1z"/></svg>
    +44 (0) 207 946 0321
  </div>
  <div class="abs top-contact" style="left:893px">
    <svg width="15" height="11" viewBox="0 0 15 11"><rect width="15" height="11" rx="1" fill="var(--green)"/><path d="M1 1l6.5 5L14 1" stroke="#111" fill="none"/></svg>
    hello@drelvix.co.uk
  </div>
  <nav class="abs nav">
    <a class="active" style="left:0">HOME</a>
    <a style="left:82px">ABOUT</a>
    <a style="left:172px">PORTFOLIO</a>
    <a style="left:290px">WHAT WE DO</a>
    <a style="left:422px">CONTACT US</a>
  </nav>
</header>

<section class="intro">
  <div class="abs brand intro-logo">DRELVIX</div>
  <h1 class="abs tagline" style="font-weight:400">Your &nbsp;Inbound Marketing &amp; SEO Performance Agency</h1>
  <p class="abs intro-copy">Do you want to earn your customers attention? Gain more visibility in the SERPs and build &amp; engage with your audience? Drelvix specialises in SEO, Social media, CRO and Design &amp; Creative services. Offering a bespoke and personal service from a team of digital natives.</p>
  <div class="abs intro-shadow"></div>
</section>

<section class="features">
  <div class="abs tile tile--services">
    <svg width="86" height="74" viewBox="0 0 86 74"><rect x="2" y="2" width="82" height="52" rx="3" fill="none" stroke="#fff" stroke-width="5"/><rect x="36" y="54" width="14" height="12" fill="#fff"/><rect x="24" y="64" width="38" height="6" rx="2" fill="#fff"/></svg>
    <p class="tile-copy">We offer a bespoke service and will customise to your needs. We specialise in progressive innovative solutions.</p>
    <div class="tile-title">What can we do for you?</div>
  </div>
  <div class="abs tile tile--portfolio">
    <svg width="80" height="94" viewBox="0 0 80 94"><rect x="37" y="0" width="6" height="8" fill="#fff"/><rect x="4" y="8" width="72" height="46" fill="none" stroke="#fff" stroke-width="5"/><path d="M40 56v14M40 58L22 92M40 58l18 34" stroke="#fff" stroke-width="5" fill="none"/></svg>
    <p class="tile-copy">Take a look at our case-studies to see our recent campaigns showing results achieved for our clients.</p>
    <div class="tile-title">See our portfolio</div>
  </div>
  <div class="abs tile tile--talk">
    <svg width="70" height="94" viewBox="0 0 70 94"><rect x="2" y="10" width="18" height="80" rx="4" fill="#fff"/><rect x="24" y="22" width="44" height="68" rx="3" fill="none" stroke="#fff" stroke-width="4"/><rect x="30" y="28" width="32" height="14" fill="#fff"/><g fill="#fff"><rect x="30" y="48" width="8" height="7"/><rect x="42" y="48" width="8" height="7"/><rect x="54" y="48" width="8" height="7"/><rect x="30" y="60" width="8" height="7"/><rect x="42" y="60" width="8" height="7"/><rect x="54" y="60" width="8" height="7"/><rect x="30" y="72" width="8" height="7"/><rect x="42" y="72" width="8" height="7"/><rect x="54" y="72" width="8" height="7"/></g></svg>
    <p class="tile-copy">Use our form to send us a message, we will call you back as soon as we can.</p>
    <div class="tile-title">Let's talk</div>
  </div>
</section>

<section class="abs work">
  <h2 class="abs section-title">Recent Work</h2>
  <p class="abs work-copy">Check out our recent works and case-studies. These are a few examples to show the diversity of work that we can do to earn real attention, generate inbound links, mentions, citations and be used across many of our marketing channels. See more on our portfolio page and learn about what we could do for you.</p>
  <svg class="abs chevron" style="left:481px" width="26" height="50" viewBox="0 0 26 50"><path d="M24 2L3 25l21 23" stroke="#e48aa8" stroke-width="2" fill="none"/></svg>
  <div class="abs monitor"></div>
  <div class="abs monitor-screen" role="img" aria-label="Campaign artwork for a travel competition showing two winners cheering in front of world landmarks"></div>
  <div class="abs monitor-stand"></div>
  <svg class="abs chevron" style="left:1016px" width="26" height="50" viewBox="0 0 26 50"><path d="M2 2l21 23L2 48" stroke="#e48aa8" stroke-width="2" fill="none"/></svg>
</section>

<section class="abs clients">
  <h2 class="abs section-title">Clients</h2>
  <p class="abs clients-copy">We work with and represent a number of progressive companies in their SEO, social, inbound marketing, content and strategy needs. Check out our case-studies for examples.</p>
  <div class="abs slider-btn" style="left:141px"><svg width="34" height="36" viewBox="0 0 34 36"><path d="M20 11l-7 7 7 7" stroke="#fff" stroke-width="2" fill="none"/></svg></div>
  <div class="abs slider-btn" style="left:178px"><svg width="34" height="36" viewBox="0 0 34 36"><path d="M14 11l7 7-7 7" stroke="#fff" stroke-width="2" fill="none"/></svg></div>
  <div class="abs client" style="left:460px"><i></i>Wayfern</div>
  <div class="abs client" style="left:665px"><i></i>Oakmarket</div>
  <div class="abs client" style="left:871px"><i></i>Staylio</div>
</section>

<section class="cta">
  <h2 class="abs section-title">Sound interesting?</h2>
  <h3 class="abs cta-sub" style="font-weight:400">Interested in what you have seen so far?</h3>
  <p class="abs cta-copy">Are you looking for a progressive and innovative inbound marketing agency who can work alongside your existing teams. If Yes, then let's have a chat.</p>
  <a class="abs cta-btn">CONTACT US</a>
</section>

<footer class="abs footer"></footer>
<div class="abs to-top"><svg width="36" height="36" viewBox="0 0 36 36"><path d="M11 21l7-7 7 7" stroke="#111" stroke-width="3" fill="none"/></svg></div>
<h2 class="abs footer-title">CONTACT</h2>
<h3 class="abs footer-sub">WHERE ARE WE?</h3>
<p class="abs footer-intro">We are in London, UK, based down the best mews in Canal Side, so come check it out and walk the canals with us or we're happy to venture to you!</p>

<div class="abs rule" style="left:141px;top:2242px;width:918px"></div>
<div class="abs vrule" style="left:380px;top:2242px;height:105px"></div>
<div class="abs vrule" style="left:610px;top:2242px;height:105px"></div>
<div class="abs vrule" style="left:840px;top:2242px;height:105px"></div>
<div class="abs rule" style="left:141px;top:2347px;width:918px"></div>
<div class="abs vrule" style="left:370px;top:2347px;height:190px"></div>
<div class="abs vrule" style="left:840px;top:2347px;height:190px"></div>

<div class="abs f-head" style="left:141px;top:2258px">UK Office</div>
<p class="abs f-body" style="left:141px;top:2290px;width:220px">7 Harrow Row, Canal Side,<br>London, UK, W2 4QX</p>
<div class="abs f-head" style="left:398px;top:2258px">Phone</div>
<p class="abs f-big" style="left:398px;top:2290px">+44 (0) 207 946 0321</p>
<div class="abs f-head" style="left:628px;top:2258px">Email</div>
<p class="abs f-big" style="left:628px;top:2290px">hello@drelvix.co.uk</p>
<div class="abs f-head" style="left:857px;top:2258px">Connect with us</div>
<div class="abs social"><i></i><i></i><i></i><i></i></div>

<div class="abs f-head" style="left:141px;top:2380px">Useful Links</div>
<ul class="abs links" style="left:141px;top:2418px">
  <li>Home</li><li>About</li><li>Portfolio</li><li>What we do</li><li>Contact us</li>
</ul>
<div class="abs f-head" style="left:398px;top:2380px">About us</div>
<p class="abs f-body" style="left:398px;top:2418px;width:420px">Drelvix is an inbound marketing agency offering a raft of services from digital strategy and planning through to SEO, Social media, SMM, CRO, Design &amp; Creative, through to paid for performance campaigns.<br><br>Talk to us to discuss your needs.</p>
<div class="abs f-head" style="left:857px;top:2380px">Search this site</div>
<div class="abs search-input">Search</div>
<div class="abs search-btn">SEARCH</div>

<div class="abs rule" style="left:141px;top:2564px;width:918px"></div>
<div class="abs brand footer-brand">DRELVIX</div>
<p class="abs legal">Copyright (c) 2013 Drelvix, All Rights Reserved.<br>Drelvix is the trading name of Drelvix Limited, registered in the UK at Companies House ID:5094417, and VAT registered ID:318 2264 07.</p>

</body>
</html>
```